Zerova Poultry "The Golden Crate"

I need a business card design and a logo design for my business. It's a delivery business of halal poultry (chicken). I would the business card to include the following information.
-business name: Zerova Poultry
-business tag line: "The Golden Crate"
Name: Tomas Velkor
Contact number: 07812450973
E-mail: zerova_fresh@mailvarn.com
Website: www.zerovapoultry.example
Also need a business logo also included relating to the business.
I would like it professional yet creative. Something original. I want it to have 2 main colours included.
I want it to have a middle Eastern/ Arabic look if possible.
Thanks :)
Target Market(s)
Butchers
Restaurants
Industry/Entity Type
Business
Contact Information for Business Card
Business name: Zerova poultry
Business tag line: "The Golden Crate"
E-mail: zerova_fresh@mailvarn.com
Name: Tomas Velkor
Look and feel

```html
<!DOCTYPE html>
<html lang="en">
<head>
<meta charset="utf-8">
<title>Zerova Poultry – Business Card</title>
<link rel="stylesheet" href="https://fonts.googleapis.com/css2?family=Mulish:wght@400;700&display=swap">
<style>
  :root {
    --stage: #8c8c8c;
    --red: #ee3524;
    --black: #0b0b0b;
    --white: #ffffff;
    --grey-text: #d8d8d8;
  }
  * { box-sizing: border-box; margin: 0; padding: 0; }
  html, body { width: 1200px; height: 900px; overflow: hidden; }
  body {
    background: var(--stage);
    font-family: "Mulish", "Century Gothic", sans-serif;
    position: relative;
  }
  .card {
    position: absolute;
    width: 560px;
    height: 320px;
    overflow: hidden;
    background: var(--red);
    box-shadow: 0 6px 18px rgba(0,0,0,.25);
  }
  .card--front { left: 570px; top: 100px; }
  .card--back  { left: 70px;  top: 480px; }

  .band { position: absolute; left: 0; width: 100%; background: var(--black); }
  .card--front .band { top: 56px; height: 208px; }
  .card--back .band--top { top: 0; height: 124px; }
  .card--back .band--bottom { bottom: 0; height: 22px; }

  .brand {
    position: absolute;
    left: 0; width: 100%;
    text-align: center;
  }
  .card--front .brand { top: 118px; }
  .card--back .brand { top: 34px; }
  .brand__name {
    display: inline-flex;
    align-items: center;
    gap: 10px;
    font-weight: 700;
    font-size: 34px;
    line-height: 40px;
    letter-spacing: .5px;
  }
  .brand__mark {
    width: 14px; height: 14px; border-radius: 50%;
    display: inline-block;
  }
  .card--front .brand__name { color: var(--red); }
  .card--front .brand__mark { background: var(--red); }
  .card--back .brand__name { color: var(--white); }
  .card--back .brand__mark { background: var(--white); }
  .brand__tagline {
    display: block;
    margin-top: 2px;
    font-weight: 400;
    font-size: 20px;
    line-height: 24px;
    color: var(--grey-text);
    padding-left: 70px;
  }
  .card--back .brand__tagline { color: var(--white); }

  .person {
    position: absolute;
    left: 24px; top: 132px;
    color: var(--white);
  }
  .person__name { font-weight: 700; font-size: 22px; line-height: 26px; }
  .person__role { font-weight: 400; font-size: 13px; line-height: 16px; }

  .contact {
    position: absolute;
    right: 24px; top: 184px;
    list-style: none;
    color: var(--white);
    font-size: 16px;
    line-height: 22px;
  }
  .contact li {
    display: flex;
    justify-content: flex-end;
    align-items: center;
    gap: 8px;
    white-space: nowrap;
  }
  .contact__icon { width: 12px; height: 12px; flex: none; }
</style>
</head>
<body>

  <section class="card card--front" aria-label="Card front">
    <div class="band"></div>
    <div class="brand">
      <span class="brand__name"><span class="brand__mark"></span>Zerova Poultry</span>
      <span class="brand__tagline">The Golden Crate</span>
    </div>
  </section>

  <section class="card card--back" aria-label="Card back">
    <div class="band band--top"></div>
    <div class="brand">
      <span class="brand__name"><span class="brand__mark"></span>Zerova Poultry</span>
      <span class="brand__tagline">The Golden Crate</span>
    </div>

    <div class="person">
      <p class="person__name">Tomas Velkor</p>
      <p class="person__role">Managing Director</p>
    </div>

    <ul class="contact">
      <li>123.456.7890
        <svg class="contact__icon" viewBox="0 0 12 12" aria-hidden="true"><path fill="#fff" d="M2 1h2l1 3-1.5 1a7 7 0 0 0 3.5 3.5L8 7l3 1v2a1 1 0 0 1-1 1A9 9 0 0 1 1 2a1 1 0 0 1 1-1z"/></svg></li>
      <li>123.456.7890
        <svg class="contact__icon" viewBox="0 0 12 12" aria-hidden="true"><rect fill="#fff" x="1" y="4" width="10" height="7" rx="1"/><rect fill="#fff" x="3" y="1" width="6" height="3"/></svg></li>
      <li>zerova_fresh@mailvarn.com
        <svg class="contact__icon" viewBox="0 0 12 12" aria-hidden="true"><rect fill="#fff" x="1" y="3" width="10" height="7"/><path d="M1 3l5 4 5-4" stroke="#ee3524" stroke-width=".9" fill="none"/></svg></li>
      <li>www.zerovapoultry.example
        <svg class="contact__icon" viewBox="0 0 12 12" aria-hidden="true"><path d="M5 7l2-2M4 6L2.5 7.5a1.8 1.8 0 0 0 2.5 2.5L6.5 8.5M8 6l1.5-1.5a1.8 1.8 0 0 0-2.5-2.5L5.5 3.5" stroke="#fff" stroke-width="1.3" fill="none"/></svg></li>
      <li>1234, Address Goes Here, Country Name, 123456
        <svg class="contact__icon" viewBox="0 0 12 14" aria-hidden="true"><path fill="#fff" d="M6 0a5 5 0 0 1 5 5c0 4-5 9-5 9S1 9 1 5a5 5 0 0 1 5-5z"/><circle cx="6" cy="5" r="2" fill="#ee3524"/></svg></li>
    </ul>

    <div class="band band--bottom"></div>
  </section>

</body>
</html>
```